Gold Buyer Business Card

We are looking for a card that catches attention and that someone will remember. It should have a listing of items that we buy as well as a legal disclaimer which will be provided upon request. We have attached our company logo and a photo of a design that I liked for your reference but lets see what the crowd can come up with.
thanks and good luck!!

We Buy Gold & Silver;
Antique Jewelry
Bent/Broken Jewelry
Bracelets
Bullion
Coins
Chains
Dental Gold
Earrings
Rings
Scrap Gold
Silverware/Flatware
Used Jewelry

"Best Price Guaranteed"
Updates

Please use graphics of gold jewelry piles. I want some white in order for someone to write on.

Reason: I am looking for more designs with gold jewelry and coins on them. thanks

Industry/Entity Type

Legal

Requirements
Must have
• I would like this to have pictures of gold and silver. Maybe some jewelry in a pile. We are a company that buys scrap gold and jewelry. I would like to see some boldness, this card is a marketing tool and it should leave an impression.
Should not have
• These cards need to promote the company not an individual, no names on the card.

```html
<!DOCTYPE html>
<html lang="en">
<head>
<meta charset="utf-8">
<title>Harbor Coast Gold Buyers – Business Card</title>
<link rel="stylesheet" href="https://fonts.googleapis.com/css2?family=Source+Sans+3:wght@400;600;700&display=swap">
<style>
  :root {
    --page-bg: #e9e9ea;
    --card-dark: #141110;
    --band-dark: #2a211c;
    --gold: #e7b94a;
    --gold-soft: #e6c062;
    --white: #ffffff;
  }
  * { box-sizing: border-box; margin: 0; padding: 0; }
  html, body {
    width: 1200px; height: 720px; overflow: hidden;
    background: var(--page-bg);
    font-family: "Source Sans 3", sans-serif;
  }
  .stage { position: relative; width: 1200px; height: 720px; }
  .card {
    position: absolute; top: 228px;
    width: 463px; height: 265px;
    overflow: hidden; background: var(--card-dark);
  }
  .card--front { left: 96px; }
  .card--back { left: 632px; }

  /* Front */
  .front__header {
    position: absolute; left: 0; top: 0; width: 100%; height: 70px;
    background: linear-gradient(90deg, #3a2a22 0%, var(--band-dark) 40%, #1f1915 100%);
    display: flex; align-items: center; justify-content: center;
  }
  .brand-name {
    color: var(--gold); font-weight: 700; font-size: 20px;
    letter-spacing: 0.3px; display: flex; align-items: center; gap: 8px;
  }
  .brand-name__mark {
    width: 10px; height: 10px; border-radius: 50%; background: var(--gold);
  }
  .front__photo {
    position: absolute; left: 0; top: 70px; width: 100%; height: 154px;
    background:
      radial-gradient(ellipse 22% 40% at 25% 65%, rgba(255,214,110,0.9) 0%, rgba(255,214,110,0) 100%),
      radial-gradient(ellipse 14% 22% at 58% 50%, rgba(170,30,50,0.75) 0%, rgba(170,30,50,0) 100%),
      radial-gradient(ellipse 30% 55% at 50% 70%, rgba(250,200,80,0.95) 0%, rgba(250,200,80,0) 100%),
      radial-gradient(ellipse 20% 50% at 80% 35%, rgba(230,170,110,0.8) 0%, rgba(230,170,110,0) 100%),
      radial-gradient(ellipse 18% 60% at 6% 30%, rgba(90,35,20,0.9) 0%, rgba(90,35,20,0) 100%),
      linear-gradient(180deg, #b95e1c 0%, #d88a2a 45%, #c8791f 100%);
  }
  .front__footer {
    position: absolute; left: 0; top: 224px; width: 100%; height: 41px;
    background: linear-gradient(180deg, #1c1714 0%, var(--card-dark) 100%);
    text-align: center;
  }
  .front__url {
    display: block; padding-top: 3px;
    color: var(--gold-soft); font-size: 12px; text-decoration: none;
  }

  /* Back */
  .back__photo {
    position: absolute; inset: 0;
    background:
      radial-gradient(ellipse 30% 35% at 88% 15%, rgba(170,130,80,0.55) 0%, rgba(170,130,80,0) 100%),
      radial-gradient(ellipse 30% 30% at 45% 25%, rgba(150,120,80,0.45) 0%, rgba(150,120,80,0) 100%),
      radial-gradient(ellipse 45% 45% at 22% 75%, rgba(140,110,70,0.5) 0%, rgba(140,110,70,0) 100%),
      radial-gradient(ellipse 35% 40% at 80% 70%, rgba(120,95,65,0.45) 0%, rgba(120,95,65,0) 100%),
      linear-gradient(160deg, #2f261d 0%, #2a221b 50%, #18130f 100%);
  }
  .back__content { position: absolute; inset: 0; }
  .back__title {
    position: absolute; top: 14px; width: 100%; text-align: center;
    color: var(--gold); font-weight: 700; font-size: 23px; line-height: 30px;
  }
  .buy-list {
    position: absolute; top: 56px; list-style: none;
    color: var(--gold-soft); font-size: 16.5px; line-height: 20.8px;
  }
  .buy-list--left { left: 88px; }
  .buy-list--right { left: 277px; }
  .back__promise {
    position: absolute; top: 187px; left: 0; width: 100%; text-align: center;
    color: var(--white); font-weight: 600; font-size: 15.5px; line-height: 22px;
    padding-left: 4px;
  }
  .contact {
    position: absolute; top: 231px; font-size: 10.5px; line-height: 14px;
    color: var(--gold-soft);
  }
  .contact b { color: var(--gold); font-weight: 700; }
  .contact--phone { left: 22px; }
  .contact--address { right: 22px; }
</style>
</head>
<body>
<main class="stage">
  <section class="card card--front" aria-label="Card front">
    <header class="front__header">
      <span class="brand-name"><span class="brand-name__mark"></span>Harbor Coast Gold Buyers Inc.</span>
    </header>
    <div class="front__photo" role="img" aria-label="Photo of a pile of gold jewelry with gold bars, rings, bracelets, gemstones, a ruby pendant and coins on glittering gold dust"></div>
    <footer class="front__footer">
      <a class="front__url" href="#">www.harborcoastgold.com</a>
    </footer>
  </section>

  <section class="card card--back" aria-label="Card back">
    <div class="back__photo" role="img" aria-label="Photo of gold bars, stacked gold and silver coins and banknotes in warm sepia tones"></div>
    <div class="back__content">
      <h1 class="back__title">We Buy Gold &amp; Silver</h1>
      <ul class="buy-list buy-list--left">
        <li>Antique Jewelry</li>
        <li>Bent/Broken Jewelry</li>
        <li>Bracelets</li>
        <li>Bullion</li>
        <li>Coins</li>
        <li>Chain</li>
      </ul>
      <ul class="buy-list buy-list--right">
        <li>Dental Gold</li>
        <li>Earrings</li>
        <li>Rings</li>
        <li>Scrap Gold</li>
        <li>Silverware/Flatware</li>
        <li>Used Jewelry</li>
      </ul>
      <p class="back__promise">Best Price Guaranteed</p>
      <p class="contact contact--phone"><b>Phone:</b> (555) 014 2290</p>
      <p class="contact contact--address"><b>Address:</b> 127 Lantern Row, Fairhaven, <b>Florida 30021</b></p>
    </div>
  </section>
</main>
</body>
</html>
```